Organic Soap Packaging

We need a package design for a new company called Fern Naturals. Our primary product is organic soap. Our business model is based on the social entrepreneurial concept of by one give one like Valo shoes. We are giving soap to help prevent the spread of disease; 1.4 million deaths a year can be prevented by hand washing.

The design is for a recycled cardboard box/package. We want to demonstrate the high end, luxury feel of the product with undertones of organic/earth friendly/social conscious.

The soap is small batch, spa like, essential oil scented all natural luxury.
Updates

I am very excited about this startup business and I believe we will have great success! I am passionate about organic personal care and helping others in need. If you share my passion, please bring your work to the table!

Target Market(s)

My target market is people who are educated through college. Health conscious, socially conscious, Generation X. Basically shoppers of Green Basket and Halvorsen.

Industry/Entity Type

Business

Requirements
Must have
• Suitable for Face, Hair, and Skin
Scented with Organic Essential Oils

```html
<!DOCTYPE html>
<html lang="en">
<head>
<meta charset="utf-8">
<title>Fern Naturals – Organic Soap Packaging</title>
<link rel="stylesheet" href="https://fonts.googleapis.com/css2?family=Gochi+Hand&family=Crimson+Text&family=Open+Sans:wght@400&display=swap">
<style>
  :root {
    --leaf: #6b8a2a;
    --sun: #e6cf3e;
    --kraft: #e4ba88;
    --kraft-dark: #d9ab78;
    --cream: #f6f0c8;
    --paper: #ffffff;
    --ink: #111111;
    --rule: #6b8a2a;
  }
  html, body {
    margin: 0;
    padding: 0;
    width: 1200px;
    height: 900px;
    overflow: hidden;
    background: var(--paper);
  }
  .canvas {
    display: block;
    width: 1200px;
    height: 900px;
  }
  .script { font-family: "Gochi Hand", cursive; fill: var(--cream); }
  .serif  { font-family: "Crimson Text", serif; fill: var(--cream); }
  .label  { font-family: "Open Sans", sans-serif; fill: var(--rule); font-size: 10px; }
  .brand  { font-family: "Gochi Hand", cursive; fill: var(--cream); }
  .fold   { fill: none; stroke: var(--rule); stroke-width: 1; }
  .panel-green { fill: var(--leaf); }
  .panel-yellow { fill: var(--sun); }
</style>
</head>
<body>
<svg class="canvas" viewBox="0 0 1200 900" xmlns="http://www.w3.org/2000/svg">
  <defs>
    <linearGradient id="kraft-board" x1="0" y1="0" x2="1" y2="1">
      <stop offset="0" stop-color="var(--kraft)"/>
      <stop offset="1" stop-color="var(--kraft-dark)"/>
    </linearGradient>
  </defs>

  <!-- page frame -->
  <rect class="top-band" x="0" y="0" width="1200" height="12" fill="var(--leaf)"/>
  <rect class="board" x="0" y="28" width="1200" height="830" fill="url(#kraft-board)"/>
  <rect class="foot-band" x="0" y="884" width="1200" height="16" fill="var(--ink)"/>

  <!-- front panel preview -->
  <g class="front-preview">
    <rect class="panel-green" x="166" y="149" width="24" height="329"/>
    <rect class="panel-green" x="166" y="149" width="26" height="21"/>
    <rect class="panel-green" x="200" y="149" width="18" height="21"/>
    <rect class="panel-green" x="226" y="149" width="152" height="21"/>
    <rect class="panel-green" x="166" y="170" width="70" height="38"/>
    <text class="brand" x="203" y="186" font-size="15" text-anchor="middle">Fern</text>
    <text class="brand" x="203" y="201" font-size="15" text-anchor="middle">Naturals</text>

    <rect class="panel-green" x="224" y="203" width="154" height="275"/>
    <g class="script" text-anchor="middle">
      <text x="300" y="256" font-size="22">Luxury</text>
      <text x="300" y="276" font-size="17">Organic</text>
      <text x="300" y="295" font-size="17">Soap</text>
      <text x="300" y="312" font-size="15">scented</text>
      <text x="300" y="328" font-size="14">with</text>
      <text x="300" y="342" font-size="12">Essential</text>
      <text x="300" y="355" font-size="10">Oils.</text>
    </g>
    <circle cx="297" cy="400" r="20" fill="var(--cream)" opacity="0.55" role="img" aria-label="Leaf wreath ornament"/>
    <g class="serif" text-anchor="middle" font-size="9.5">
      <text x="301" y="448">This product is suitable</text>
      <text x="301" y="461">for Face, Hair and Body.</text>
    </g>
  </g>

  <!-- box dieline -->
  <g class="dieline">
    <path class="fold" d="M625 232 L636 200 L640 188 L766 188 L770 200 L777 232"/>
    <text class="label" x="695" y="216" text-anchor="middle">top</text>
    <path class="fold" d="M625 637 L636 669 L640 682 L766 682 L770 669 L777 637"/>
    <text class="label" x="700" y="662" text-anchor="middle">bottom</text>
    <path class="fold" d="M1015 317 L1060 330 L1060 540 L1015 552"/>
    <text class="label" x="1036" y="437" text-anchor="middle">glue</text>
    <path class="fold" d="M922 637 L930 670 L930 682 L958 682 L958 670 L966 637"/>

    <path class="panel-yellow" d="M576 232 L638 232 L638 632 L576 632 L538 592 L538 272 Z"/>
    <rect class="panel-yellow" x="662" y="232" width="115" height="405"/>
    <path class="panel-yellow" d="M777 232 L822 240 L860 272 L860 592 L822 630 L777 637 Z"/>
    <rect class="panel-yellow" x="860" y="317" width="155" height="320"/>

    <rect class="kraft-gap" x="538" y="331" width="240" height="23" fill="var(--kraft)"/>
    <rect class="kraft-gap" x="860" y="331" width="155" height="23" fill="var(--kraft)"/>

    <rect class="panel-green" x="625" y="317" width="152" height="13"/>
    <path class="panel-green" d="M862 317 L910 317 L906 330 L862 330 Z"/>
    <path class="panel-green" d="M968 317 L1015 317 L1015 330 L964 330 Z"/>
    <rect class="panel-green" x="625" y="317" width="13" height="235"/>
    <rect class="panel-green" x="607" y="328" width="86" height="30"/>
    <text class="brand" x="650" y="341" font-size="12" text-anchor="middle">Fern</text>
    <text class="brand" x="650" y="354" font-size="12" text-anchor="middle">Naturals</text>

    <rect class="panel-green" x="662" y="354" width="115" height="198"/>
    <g class="script" text-anchor="middle">
      <text x="716" y="386" font-size="15">Luxury</text>
      <text x="714" y="400" font-size="12">Organic</text>
      <text x="714" y="413" font-size="12">Soap</text>
      <text x="714" y="425" font-size="11">scented</text>
      <text x="714" y="436" font-size="10">with</text>
      <text x="714" y="446" font-size="9">Essential</text>
      <text x="714" y="455" font-size="7.5">Oils.</text>
    </g>
    <circle cx="713" cy="484" r="15" fill="var(--cream)" opacity="0.55" role="img" aria-label="Leaf wreath ornament"/>
    <g class="serif" text-anchor="middle" font-size="7">
      <text x="717" y="524">This product is suitable</text>
      <text x="717" y="533">for Face, Hair and Body.</text>
    </g>

    <rect class="panel-green" x="862" y="354" width="153" height="198"/>
    <g class="serif" text-anchor="middle" font-size="9">
      <text class="script" x="938" y="388" font-size="11">Buy 1</text>
      <text class="script" x="938" y="402" font-size="11">Give 1</text>
      <text x="938" y="414">and</text>
      <text x="938" y="426">help</text>
      <text x="938" y="437">us</text>
      <text x="938" y="448">prevent</text>
      <text x="938" y="459">the</text>
      <text x="938" y="470">spread</text>
      <text x="938" y="481">of</text>
      <text x="938" y="492">disease;</text>
      <text x="938" y="527">1.4 million deaths a year</text>
      <text x="938" y="538">can be prevented by hand washing.</text>
    </g>
  </g>

  <!-- faint decorative border at foot -->
  <rect x="140" y="715" width="880" height="36" rx="18" fill="var(--sun)" opacity="0.18" role="img" aria-label="Faint leaf pattern decoration"/>
</svg>
</body>
</html>
```